Larkspur Ridge Management - Business Cards

I need business cards. My current logo was designed by a designer at this site and I very much like and am happy with the results. I would like a business card that is trendy, unique, current yet professional. I deal with high net worth clients daily

Target Market(s)

Out of state investors looking to get into the rental market in Ohio

Industry/Entity Type

Property Management, Consulting

Contact Information for Business Card

Name, Title (Chief Financial Officer) office phone number (555) 817-3094 website address larkridgemgmt.example

Font styles to use
Sans Serif

Colors
0054AA
0677BA
7BADD7
CADEEF
E8F1F8
0094D4
00A9DD
6FCCEA
C7EBF8
E9F6FB
00AB8E
00BBA5
67D7C9
C6EFE9
E9F9F6

```html
<!DOCTYPE html>
<html lang="en">
<head>
<meta charset="utf-8">
<title>Larkspur Ridge Management – Business Cards</title>
<link href="https://fonts.googleapis.com/css2?family=Arimo:wght@400;700&display=swap" rel="stylesheet">
<style>
  :root {
    --backdrop: #e4e4e2;
    --card-blue: #365f93;
    --region-blue: #2f5282;
    --ink-white: #ffffff;
    --accent-red: #d9302f;
    --card-shadow: rgba(0, 0, 0, 0.22);
  }
  * { margin: 0; padding: 0; box-sizing: border-box; }
  html, body {
    width: 1200px; height: 900px; overflow: hidden;
    background: var(--backdrop);
    font-family: "Arimo", Arial, sans-serif;
    color: var(--ink-white);
  }
  .sheet { position: relative; width: 1200px; height: 900px; }

  .card {
    position: absolute;
    width: 560px; height: 320px;
    background: var(--card-blue);
    box-shadow: 0 14px 30px var(--card-shadow);
    overflow: hidden;
  }
  .card--front { left: 110px; top: 90px; }
  .card--back  { left: 530px; top: 490px; }

  .region-fill {
    position: absolute;
    left: 40px; top: 70px; width: 180px; height: 230px;
    background: var(--region-blue);
    border-radius: 18px 40px 30px 22px;
    opacity: 0.85;
  }
  .card-frame { position: absolute; inset: 0; }

  /* front */
  .front-stack {
    position: absolute; left: 0; right: 0; top: 78px;
    display: flex; flex-direction: column; align-items: center; gap: 22px;
  }
  .holder-name { font-size: 22px; font-weight: 700; letter-spacing: 0.5px; }
  .brand-name {
    display: flex; align-items: center; gap: 12px;
    font-size: 26px; font-weight: 700; text-align: center; line-height: 1.15;
  }
  .brand-mark { width: 18px; height: 18px; background: var(--accent-red); flex: none; }

  /* back */
  .identity { position: absolute; left: 120px; top: 58px; width: 270px; }
  .identity-name { font-size: 40px; font-weight: 700; letter-spacing: 0.5px; line-height: 1; }
  .identity-title { font-size: 19px; font-weight: 700; margin-top: 6px; }
  .identity-rule { height: 2px; background: var(--ink-white); margin-top: 8px; }

  .brand-name--small {
    position: absolute; right: 36px; top: 70px; width: 130px;
    font-size: 17px; flex-direction: column; gap: 8px;
  }
  .brand-name--small .brand-mark { width: 12px; height: 12px; }

  .contact-list {
    position: absolute; left: 46px; top: 176px;
    list-style: none; display: flex; flex-direction: column; gap: 12px;
  }
  .contact-item { display: flex; align-items: center; gap: 12px; font-size: 19px; font-weight: 700; }
  .contact-item small { font-size: 14px; font-weight: 400; margin-left: 4px; }
  .contact-icon { width: 20px; height: 20px; flex: none; }
</style>
</head>
<body>
<main class="sheet">

  <section class="card card--front" aria-label="Business card front">
    <div class="region-fill" role="img" aria-label="Faint silhouette map of Ohio"></div>
    <svg class="card-frame" viewBox="0 0 560 320" aria-hidden="true">
      <rect x="24" y="24" width="512" height="272" fill="none" stroke="#fff" stroke-width="1.5" stroke-dasharray="1.5 3.5"/>
      <g stroke="#fff" stroke-width="1.5">
        <line x1="150" y1="16" x2="150" y2="32"/><line x1="410" y1="16" x2="410" y2="32"/>
        <line x1="150" y1="288" x2="150" y2="304"/><line x1="410" y1="288" x2="410" y2="304"/>
        <line x1="16" y1="110" x2="32" y2="110"/><line x1="528" y1="210" x2="544" y2="210"/>
      </g>
    </svg>
    <div class="front-stack">
      <p class="holder-name">JOHN DOE</p>
      <p class="brand-name"><span class="brand-mark"></span>Larkspur Ridge<br>Management</p>
    </div>
  </section>

  <section class="card card--back" aria-label="Business card back">
    <div class="region-fill" role="img" aria-label="Faint silhouette map of Ohio"></div>
    <svg class="card-frame" viewBox="0 0 560 320" aria-hidden="true">
      <rect x="24" y="24" width="512" height="272" fill="none" stroke="#fff" stroke-width="1.5" stroke-dasharray="1.5 3.5"/>
      <g stroke="#fff" stroke-width="1.5">
        <line x1="150" y1="16" x2="150" y2="32"/><line x1="410" y1="16" x2="410" y2="32"/>
        <line x1="150" y1="288" x2="150" y2="304"/><line x1="410" y1="288" x2="410" y2="304"/>
        <line x1="16" y1="110" x2="32" y2="110"/><line x1="528" y1="210" x2="544" y2="210"/>
      </g>
    </svg>

    <div class="identity">
      <h1 class="identity-name">JOHN DOE</h1>
      <p class="identity-title">Chief Financial Officer</p>
      <div class="identity-rule"></div>
    </div>

    <p class="brand-name brand-name--small"><span class="brand-mark"></span>Larkspur Ridge Management</p>

    <ul class="contact-list">
      <li class="contact-item">
        <svg class="contact-icon" viewBox="0 0 24 24" aria-hidden="true"><path d="M6.6 10.8a15 15 0 0 0 6.6 6.6l2.2-2.2a1 1 0 0 1 1-.25 11.4 11.4 0 0 0 3.6.6 1 1 0 0 1 1 1V20a1 1 0 0 1-1 1A17 17 0 0 1 3 4a1 1 0 0 1 1-1h3.5a1 1 0 0 1 1 1c0 1.25.2 2.45.6 3.6a1 1 0 0 1-.25 1z" fill="#fff"/></svg>
        <span>(555) 817-3094<small>Office Call/Text</small></span>
      </li>
      <li class="contact-item">
        <svg class="contact-icon" viewBox="0 0 24 24" aria-hidden="true" fill="none" stroke="#fff" stroke-width="2"><circle cx="12" cy="12" r="9.5"/><ellipse cx="12" cy="12" rx="4" ry="9.5"/><line x1="2.5" y1="12" x2="21.5" y2="12"/></svg>
        <span>larkridgemgmt.example</span>
      </li>
      <li class="contact-item">
        <svg class="contact-icon" viewBox="0 0 24 24" aria-hidden="true" fill="none" stroke="#fff" stroke-width="2"><rect x="2" y="5" width="20" height="14"/><path d="M2 5l10 8 10-8"/></svg>
        <span>info@larkspurridgemgmt.example</span>
      </li>
    </ul>
  </section>

</main>
</body>
</html>
```